Need to drive pregnant women to my 3d4d ultrasound studio where i provide 4d ultrasound with hyperalistic imaging and gender reveals

Industry/Entity Type

Healthcare

Font styles to use
Decorative
Script

Requirements
Must have
• My Company name Luz de Nueve Lunas 4D. EVERYTHING HAS TO BE IN SPANISH
Nice to have
• SIMPLE AND NOT TOO BUSY
Should not have
• website

```html
<!DOCTYPE html>
<html lang="es">
<head>
<meta charset="UTF-8">
<title>Luz de Nueve Lunas 4D</title>
<link rel="stylesheet" href="https://fonts.googleapis.com/css2?family=Grand+Hotel&family=Playfair+Display:wght@700&family=Lato:wght@400&display=swap">
<style>
  :root {
    --pink-main: #fb2a93;
    --pink-light: #ff45a6;
    --pink-deep: #e81f86;
    --ribbon: #ffb3cf;
    --ribbon-edge: #ffd6e6;
    --heart: #ff5fb0;
    --white: #ffffff;
    --ink: #1b1b1b;
    --purple: #a0267f;
    --skin: #efcdbf;
    --skin-light: #f6e2d8;
    --skin-dark: #d9b3a3;
    --cloth: #f3f1f1;
    --scan: #b5631e;
    --scan-dark: #5e2a08;
  }
  * { margin: 0; padding: 0; box-sizing: border-box; }
  html, body { width: 1200px; height: 350px; overflow: hidden; background: var(--white); }
  .banner {
    position: relative;
    width: 1200px;
    height: 350px;
    overflow: hidden;
    background: radial-gradient(ellipse at 40% 40%, var(--pink-light), var(--pink-main) 55%, var(--pink-deep));
  }
  .floral-area {
    position: absolute;
    left: 0; top: 190px;
    width: 200px; height: 160px;
    background: radial-gradient(ellipse at 45% 60%, rgba(255,220,235,0.35), rgba(255,220,235,0) 70%);
  }
  .photo-belly {
    position: absolute;
    left: 671px; top: 0;
    width: 529px; height: 350px;
    background:
      radial-gradient(ellipse 200px 150px at 260px 175px, var(--skin-dark) 0%, var(--skin) 55%, rgba(239,205,191,0) 100%),
      linear-gradient(180deg, var(--cloth) 0%, var(--cloth) 12%, var(--skin-light) 26%, var(--skin-light) 76%, var(--cloth) 88%),
      var(--cloth);
  }
  .photo-belly::after {
    content: "";
    position: absolute;
    right: 0; top: 0;
    width: 60px; height: 350px;
    background: linear-gradient(90deg, rgba(160,38,127,0), var(--purple));
  }
  .brand { font-weight: normal; }
  .brand-script {
    position: absolute;
    left: 100px; top: 44px;
    font-family: "Grand Hotel", cursive;
    font-size: 100px;
    line-height: 1;
    color: var(--white);
    white-space: nowrap;
  }
  .brand-serif {
    position: absolute;
    left: 198px; top: 150px;
    font-family: "Playfair Display", serif;
    font-weight: 700;
    font-size: 68px;
    line-height: 1;
    letter-spacing: 1px;
    color: var(--white);
    white-space: nowrap;
  }
  .ribbon {
    position: absolute;
    top: 250px;
    width: 246px; height: 36px;
  }
  .ribbon-shape { position: absolute; left: 0; top: 0; width: 246px; height: 36px; }
  .ribbon-label {
    position: absolute;
    left: 0; top: 0; width: 246px; height: 36px;
    display: flex; align-items: center; justify-content: center;
    font-family: "Lato", sans-serif;
    font-size: 17px;
    letter-spacing: 0.3px;
    color: var(--ink);
  }
  .ribbon-heart {
    position: absolute;
    top: -10px; left: 114px;
    width: 18px; height: 16px;
  }
  .ribbon-imagen { left: 122px; }
  .ribbon-genero { left: 383px; }
  .photo-circle {
    position: absolute;
    top: 192px;
    width: 134px; height: 134px;
    border-radius: 50%;
    border: 4px solid var(--white);
  }
  .photo-scan {
    left: 655px;
    background: radial-gradient(circle at 55% 55%, var(--scan), var(--scan-dark) 85%);
  }
  .photo-newborn {
    left: 772px;
    background: radial-gradient(circle at 50% 55%, #f3dccf, var(--skin-dark) 90%);
  }
</style>
</head>
<body>
<main class="banner">
  <div class="photo-belly" role="img" aria-label="Foto de una mujer embarazada formando un corazón con las manos sobre el vientre"></div>
  <div class="floral-area" role="img" aria-label="Ornamento floral con ramas y hojas en rosa claro"></div>

  <h1 class="brand">
    <span class="brand-script">Luz de Nueve</span>
    <span class="brand-serif">LUNAS 4D</span>
  </h1>

  <div class="ribbon ribbon-imagen">
    <svg class="ribbon-shape" viewBox="0 0 246 36" preserveAspectRatio="none" aria-hidden="true">
      <polygon points="0,0 246,0 232,18 246,36 0,36 14,18" fill="var(--ribbon)"/>
      <polygon points="6,3 240,3 228,18 240,33 6,33 18,18" fill="none" stroke="var(--ribbon-edge)" stroke-width="1.5"/>
    </svg>
    <svg class="ribbon-heart" viewBox="0 0 20 18" aria-hidden="true">
      <path d="M10 17 C2 11 0 7 3 3 C6 0 9 2 10 4 C11 2 14 0 17 3 C20 7 18 11 10 17Z" fill="var(--heart)"/>
    </svg>
    <span class="ribbon-label">IMAGEN HIPERALISTA</span>
  </div>

  <div class="ribbon ribbon-genero">
    <svg class="ribbon-shape" viewBox="0 0 246 36" preserveAspectRatio="none" aria-hidden="true">
      <polygon points="0,0 246,0 232,18 246,36 0,36 14,18" fill="var(--ribbon)"/>
      <polygon points="6,3 240,3 228,18 240,33 6,33 18,18" fill="none" stroke="var(--ribbon-edge)" stroke-width="1.5"/>
    </svg>
    <svg class="ribbon-heart" viewBox="0 0 20 18" aria-hidden="true">
      <path d="M10 17 C2 11 0 7 3 3 C6 0 9 2 10 4 C11 2 14 0 17 3 C20 7 18 11 10 17Z" fill="var(--heart)"/>
    </svg>
    <span class="ribbon-label">EL GÉNERO REVELA</span>
  </div>

  <div class="photo-circle photo-scan" role="img" aria-label="Imagen de ecografía 4D de un bebé"></div>
  <div class="photo-circle photo-newborn" role="img" aria-label="Foto de un bebé recién nacido dormido"></div>
</main>
</body>
</html>
```